New flavour! New packaging for Velocity Energy Drink!

We need a new packaging designed to show off our new grape flavored energy drink! It will require box design with matching sachets!

Established in 2018 we are a fully Australian owned and operated business that started out with 2 gamers that got sick and tired of sugary energy drinks OR expensive powder from the USA.

We are an energy drink in the esports and gaming space. Our new product is an energy drink in powder in boxes of 30 sachets (please see attached for product example)

Please see example 1 and 2 for our competitors product. We would ideally like to go a bit more minimalist than them but still have a great color pop on black backing.

Target Market(s)

Gamer's and esports athletes between the ages or 18-30

Font styles to use
Sans Serif
Other font styles liked:
• Helvetica

Colors
886aae
ffffff

Requirements
Must have
• Black base/background.
• Vibrant purple N in the Velocity Logo.
• Same or slightly different shades of purple for some text and highlights.
• Black, white and some shades of a vibrant purple (for the grape flavor)
• ingredients list (may need to be reformatted to suit)
• Please see attached for legislative requirements on the box and sachets.
Nice to have
• minimalist design but enough to be eye catching and somewhat playful
• Twitter: @VLCT_FUEL
• Instagram: @VLCT_FUEL
• Facebook: @VLCTFUEL
Should not have
• OTHER COLORS.
• Overly complex designs.

```html
<!DOCTYPE html>
<html lang="en">
<head>
<meta charset="UTF-8">
<title>Velocity Energy Drink – Grape Box Panels</title>
<link rel="stylesheet" href="https://fonts.googleapis.com/css2?family=Montserrat:wght@400;500;600;800&family=Oswald:wght@400;500;600&display=swap">
<style>
  :root {
    --stage: #e9eef3;
    --black: #0b0a0d;
    --charcoal: #1c1a20;
    --purple: #886aae;
    --purple-deep: #4a3a63;
    --purple-dark: #2a2235;
    --white: #ffffff;
    --muted: #d9d2e4;
    --water: #7fb6d8;
    --grape: #3b3566;
  }
  * { margin: 0; padding: 0; box-sizing: border-box; }
  html, body { width: 1200px; height: 977px; overflow: hidden; }
  body { background: var(--stage); font-family: "Montserrat", Helvetica, Arial, sans-serif; color: var(--white); }

  .dieline { position: absolute; left: 175px; top: 108px; width: 850px; height: 760px; display: flex; box-shadow: 0 18px 40px rgba(0,0,0,.25); }

  /* Side panel */
  .side-panel { position: relative; width: 270px; height: 100%; overflow: hidden;
    background: radial-gradient(ellipse at 30% 40%, var(--purple-deep) 0%, var(--purple-dark) 55%, var(--black) 100%); }
  .side-panel .brand { position: absolute; left: 34px; top: 62px; }
  .brand-name { font-family: "Montserrat", sans-serif; font-weight: 800; color: var(--white); letter-spacing: .02em; line-height: 1; display: flex; align-items: center; gap: 8px; }
  .brand-name .mark { display: inline-block; background: var(--purple); }
  .side-panel .brand-name { font-size: 26px; }
  .side-panel .brand-name .mark { width: 12px; height: 12px; }
  .brand-sub { font-weight: 500; letter-spacing: .28em; text-transform: uppercase; color: var(--white); }
  .side-panel .brand-sub { font-size: 7px; margin-top: 5px; margin-left: 58px; }

  .info { position: absolute; left: 34px; top: 128px; width: 200px; }
  .info h3 { font-family: "Oswald", sans-serif; font-weight: 500; font-size: 15px; display: inline-block; border-bottom: 1px solid var(--white); padding-bottom: 1px; margin-bottom: 7px; }
  .info p { font-size: 9.5px; line-height: 1.45; color: var(--muted); margin-bottom: 10px; }
  .info .warning { font-family: "Oswald", sans-serif; font-size: 12px; color: var(--white); font-weight: 500; }

  .athlete-photo { position: absolute; left: 0; bottom: 0; width: 270px; height: 340px;
    background: linear-gradient(180deg, rgba(136,106,174,0) 0%, rgba(200,195,210,.55) 55%, rgba(230,228,236,.8) 100%); }

  /* Front panel */
  .front-panel { position: relative; width: 580px; height: 100%; overflow: hidden;
    background: linear-gradient(135deg, var(--charcoal) 0%, var(--black) 45%, var(--charcoal) 100%); }
  .front-panel .brand { position: absolute; left: 140px; top: 80px; }
  .front-panel .brand-name { font-size: 58px; }
  .front-panel .brand-name .mark { width: 22px; height: 22px; }
  .front-panel .brand-sub { font-size: 13px; margin-top: 8px; text-align: right; }

  .headline { position: absolute; right: 50px; top: 225px; text-align: center; width: 300px; }
  .headline .line-1 { font-family: "Oswald", sans-serif; font-weight: 600; font-size: 108px; line-height: 1; letter-spacing: .01em; }
  .headline .line-2 { font-family: "Oswald", sans-serif; font-weight: 400; font-size: 76px; line-height: 1.05; }

  .flavour-tag { position: absolute; right: 50px; top: 420px; background: var(--purple); color: var(--white);
    font-weight: 600; font-size: 19px; letter-spacing: .22em; padding: 6px 14px 6px 20px; }
  .ingredients-line { position: absolute; right: 76px; top: 470px; font-size: 16px; font-weight: 500; }

  .splash-fruit { position: absolute; left: 0; bottom: 0; width: 580px; height: 300px;
    background: radial-gradient(ellipse at 40% 65%, var(--grape) 0%, rgba(59,53,102,.6) 28%, rgba(127,182,216,.35) 55%, rgba(11,10,13,0) 80%); }
  .water-band { position: absolute; left: 0; bottom: 0; width: 580px; height: 38px;
    background: linear-gradient(180deg, rgba(127,182,216,.5), var(--water)); }

  .serves-badge { position: absolute; left: 0; bottom: 38px; width: 92px; height: 108px; background: var(--purple);
    text-align: center; font-family: "Oswald", sans-serif; }
  .serves-badge .count { font-size: 58px; font-weight: 600; line-height: 1; padding-top: 10px; display: block; }
  .serves-badge .unit { font-size: 18px; font-weight: 400; letter-spacing: .04em; display: block; margin-top: 4px; }

  .tagline { position: absolute; right: 20px; bottom: 50px; font-family: "Oswald", sans-serif; font-size: 13px; font-weight: 500; text-transform: uppercase; }
</style>
</head>
<body>
  <main class="dieline">
    <section class="side-panel">
      <div class="brand">
        <div class="brand-name"><span class="mark"></span>VELOCITY</div>
        <div class="brand-sub">Energy Drink</div>
      </div>
      <div class="info">
        <h3>Storage statement:</h3>
        <p>Store in a cool dry place, away from sunlight below 25°C.<br><span class="warning">Keep away from children</span></p>
        <h3>Directions for Use:</h3>
        <p>Place one tablet in 400 ml water, stir until dissolved, and consume immediately.</p>
        <h3>Usage:</h3>
        <p>Maximum of two<br>tablets per day</p>
        <h3>Best Before:</h3>
        <p>See base of packaging</p>
      </div>
      <div class="athlete-photo" role="img" aria-label="Photo of a tennis player mid-swing in an orange shirt, with soft smoke behind"></div>
    </section>

    <section class="front-panel">
      <div class="brand">
        <div class="brand-name"><span class="mark"></span>VELOCITY</div>
        <div class="brand-sub">Energy Drink</div>
      </div>
      <h1 class="headline"><span class="line-1">ENERGY</span><br><span class="line-2">DRINK</span></h1>
      <div class="flavour-tag">GRAPE FLAVOUR</div>
      <div class="ingredients-line">With Ginseng &amp; Caffeine</div>
      <div class="splash-fruit" role="img" aria-label="Bunch of purple grapes with green leaves and a blue water splash"></div>
      <div class="water-band" role="img" aria-label="Blue water surface"></div>
      <div class="serves-badge"><span class="count">30</span><span class="unit">SERVES</span></div>
      <div class="tagline">For gamers, by gamers</div>
    </section>
  </main>
</body>
</html>
```